Hey There Pinecrest....a heavily based video and picture gallery style website.

Would like a multipage website for videos and pictures. For example, one page/category will be Events. I would like that page to be a thumbnail gallery where the user would click on a thumbnail and the video will play over/hover the the thumbnail page(not go to another page). So when the user closes the player, they are still on the events page. On each page, would like a navigation bar to be able to go to the other pages/categories. And I would like it this way for the other categories as well (people, places, meet the vendors, pictures....) Please view my current website for all pages needed. I only submitted a fraction of images. How should i send the videos? Please contact if questions.
My current website is at www.heytherepinecrest.example

Target Market(s)

male/female, 30-70+ years old

Industry/Entity Type

Entertainment

Coding

Coded - Design and coding required

Number of Pages Required

5+ page

Font styles to use
Sans Serif

Colors
0393ce
00a990
f04a51
f68d4e

Requirements
Must have
• social media links. the video player must play/hover over the current page rather than going to another page. my logo. a calendar page where I can add events to it. a text area under videos for description, photo gallery for each category, the ability to copy a page to use as a template to add more videos and pictures in the future, contact page, the ability to add google ads, affiliate advertising.

```html
<!DOCTYPE html>
<html lang="en">
<head>
<meta charset="utf-8">
<title>Hey There Pinecrest</title>
<link rel="stylesheet" href="https://fonts.googleapis.com/css2?family=Roboto:wght@300;400;500;700&display=swap">
<style>
:root{
  --blue:#0393ce;
  --teal:#00a990;
  --red:#f04a51;
  --orange:#f68d4e;
  --ink:#333;
  --muted:#666;
  --line:#ddd;
  --footer:#2a2a2a;
  --footer-deep:#1c1c1c;
  --footer-text:#9a9a9a;
  --white:#fff;
}
*{box-sizing:border-box;margin:0;padding:0}
html,body{width:1200px;height:2675px;overflow:hidden}
body{position:relative;background:var(--white);font-family:'Roboto',Arial,sans-serif;color:var(--ink)}

/* hero */
.hero{position:absolute;left:0;top:0;width:1200px;height:619px;overflow:hidden}
.hero-photo{position:absolute;inset:0;background:
  linear-gradient(180deg,#3c4a5a 0%,#56606a 22%,#4a4a3c 45%,#5a4a32 62%,#2e3438 80%,#3a3a36 100%)}
.hero-shade{position:absolute;inset:0;background:rgba(10,20,30,.25)}
.follow{position:absolute;left:160px;top:30px;display:flex;align-items:center;gap:5px;color:var(--white);font-size:11px;font-weight:700;letter-spacing:.5px}
.follow span{margin-right:6px}
.dot{width:20px;height:20px;border-radius:50%;background:var(--blue);display:inline-block}
.follow .dot{background:var(--white)}
.brand{position:absolute;left:476px;top:0;width:250px;height:82px}
.brand svg{position:absolute;inset:0}
.brand-name{position:absolute;left:0;right:0;top:30px;text-align:center;font-size:17px;font-weight:700;color:#0b6a8e;letter-spacing:.3px}
.search{position:absolute;left:797px;top:23px;width:241px;height:33px;border:1px solid rgba(255,255,255,.7);display:flex;align-items:center}
.search span{flex:1;padding-left:10px;color:var(--white);font-size:9px;letter-spacing:.5px}
.search i{width:31px;height:31px;background:var(--white);display:flex;align-items:center;justify-content:center}
.main-nav{position:absolute;left:160px;top:103px;width:878px;height:37px;border-top:1px solid rgba(255,255,255,.55);border-bottom:1px solid rgba(255,255,255,.55);display:flex;justify-content:center}
.main-nav a{display:block;height:35px;line-height:35px;padding:0 14px;color:var(--white);font-size:9.5px;letter-spacing:.5px;text-decoration:none}
.main-nav a.active{background:var(--blue)}
.hero-title{position:absolute;left:0;right:0;top:236px;text-align:center;color:var(--white);font-size:35px;font-weight:700;letter-spacing:2.5px}
.hero-play{position:absolute;left:583px;top:348px}
.slide-arrow{position:absolute;top:273px;width:52px;height:53px;background:var(--blue);display:flex;align-items:center;justify-content:center}
.slide-arrow.prev{left:0}
.slide-arrow.next{right:0}

/* section titles */
.section-title{position:absolute;left:0;width:1200px;text-align:center;color:var(--blue);font-size:18px;font-weight:400;letter-spacing:1.5px}
.section-title svg{display:block;margin:6px auto 0}

/* thumbnails */
.grid{position:absolute;left:160px;width:880px;display:grid;grid-template-columns:repeat(4,203px);column-gap:22px}
.grid.uploads{grid-auto-rows:180px;row-gap:5px}
.card{position:relative}
.card::before{content:"";display:block;height:5px;background:#d8d8d8}
.thumb{position:relative;height:132px}
.card-label{margin-top:12px;text-align:center;font-size:9.5px;color:#555;letter-spacing:.8px;text-transform:uppercase;line-height:14px;padding:0 6px}
.play{position:absolute;left:50%;top:50%;width:50px;height:50px;margin:-25px 0 0 -25px;background:rgba(20,20,20,.7);display:flex;align-items:center;justify-content:center}

/* feature */
.feature-media{position:absolute;left:160px;top:1860px;width:428px;height:246px;background:linear-gradient(135deg,#3a0d1c,#8a2846 45%,#c24a7c 60%,#2a0a14)}
.corner-go{position:absolute;right:0;bottom:0;width:52px;height:52px;background:var(--blue);display:flex;align-items:center;justify-content:center}
.feature-title{position:absolute;left:160px;top:2120px;font-size:16px;font-weight:400;color:var(--blue);letter-spacing:1px}
.feature-text{position:absolute;left:160px;top:2152px;width:428px;font-size:11px;line-height:22px;color:var(--muted)}
.story{position:absolute;left:611px;width:427px;height:90px}
.story-img{position:absolute;left:0;top:0;width:128px;height:82px}
.story-img .corner-go{width:26px;height:26px}
.story h3{position:absolute;left:144px;top:0;font-size:11.5px;font-weight:400;color:var(--blue);letter-spacing:.8px;text-transform:uppercase}
.story p{position:absolute;left:144px;top:22px;width:283px;font-size:10.5px;line-height:19px;color:var(--muted)}

/* contact band */
.contact-band{position:absolute;left:160px;top:2232px;width:878px;height:81px;background:var(--blue);display:flex;z-index:2}
.contact-band .cell{flex:1;display:flex;align-items:center;padding-left:38px;gap:16px;color:var(--white);font-size:10.5px;line-height:17px;border-left:1px solid rgba(255,255,255,.3)}
.contact-band .cell:first-child{border-left:none}
.contact-band .ic{width:32px;height:32px;border-radius:50%;border:1px solid rgba(255,255,255,.7);display:flex;align-items:center;justify-content:center;flex:none}

/* footer */
.site-footer{position:absolute;left:0;top:2268px;width:1200px;height:341px;background:var(--footer)}
.foot-col{position:absolute;top:86px}
.foot-col h4{font-size:12px;font-weight:700;color:var(--blue);letter-spacing:.8px;margin-bottom:26px}
.foot-brand{font-size:17px;font-weight:700;color:#b9b9b9;width:140px;line-height:22px;margin-bottom:18px}
.foot-text{font-size:11px;line-height:18px;color:var(--footer-text)}
.services{display:grid;grid-template-columns:112px 110px;row-gap:10px}
.services li{list-style:none;font-size:11px;color:var(--footer-text);display:flex;align-items:center;gap:8px;height:16px}
.bullet{width:11px;height:11px;border-radius:50%;background:#bbb;display:flex;align-items:center;justify-content:center;flex:none}
.foot-event{display:flex;gap:10px;margin-bottom:10px;height:40px;align-items:flex-start}
.foot-event i{width:54px;height:38px;flex:none;border:2px solid #777}
.foot-event span{font-size:11px;line-height:16px;color:#ccc;text-transform:uppercase;width:150px}
.newsletter-field{margin-top:20px;width:202px;height:36px;border:2px solid #888;display:flex;align-items:center}
.newsletter-field span{flex:1;padding-left:10px;font-size:10.5px;color:#ccc}
.newsletter-field i{width:32px;height:32px;display:flex;align-items:center;justify-content:center;border-left:1px solid #666}
.foot-social{display:flex;gap:8px}
.foot-social .dot{background:#777;width:24px;height:24px}
.copyright{position:absolute;left:0;top:2609px;width:1200px;height:66px;background:var(--footer-deep);color:#888;font-size:9.5px;letter-spacing:.5px;text-align:center;line-height:66px}
</style>
</head>
<body>

<header class="hero">
  <div class="hero-photo" role="img" aria-label="Photo of a rocky river bed with autumn trees and mountains in the distance"></div>
  <div class="hero-shade"></div>

  <div class="follow"><span>FOLLOW US ON</span><i class="dot"></i><i class="dot"></i><i class="dot"></i><i class="dot"></i></div>

  <div class="brand">
    <svg width="250" height="82" viewBox="0 0 250 82"><polygon points="0,0 250,0 222,82 28,82" fill="#cfd3d6"/><polygon points="12,0 238,0 214,74 36,74" fill="#fff"/></svg>
    <div class="brand-name">Hey There Pinecrest</div>
  </div>

  <div class="search"><span>ENTER YOUR SEARCH</span><i><svg width="12" height="12" viewBox="0 0 12 12"><circle cx="5" cy="5" r="3.8" fill="none" stroke="#333" stroke-width="1.6"/><line x1="7.8" y1="7.8" x2="11" y2="11" stroke="#333" stroke-width="1.8"/></svg></i></div>

  <nav class="main-nav">
    <a class="active">HOME</a><a>VIDEOS ▾</a><a>PHOTO GALLERY ▾</a><a>CALENDAR</a><a>CONTACT</a>
  </nav>

  <h1 class="hero-title">WELCOME TO HEY THERE PINECREST</h1>
  <svg class="hero-play" width="46" height="50" viewBox="0 0 46 50"><polygon points="5,4 41,25 5,46" fill="none" stroke="#fff" stroke-width="3"/></svg>

  <div class="slide-arrow prev"><svg width="16" height="14" viewBox="0 0 16 14"><path d="M8 1 L2 7 L8 13 M2 7 H15" fill="none" stroke="#fff" stroke-width="2.4"/></svg></div>
  <div class="slide-arrow next"><svg width="16" height="14" viewBox="0 0 16 14"><path d="M8 1 L14 7 L8 13 M14 7 H1" fill="none" stroke="#fff" stroke-width="2.4"/></svg></div>
</header>

<h2 class="section-title" style="top:660px">RECENT UPLOADS<svg width="30" height="6" viewBox="0 0 30 6"><path d="M1 5 Q15 -1 29 5" fill="none" stroke="#0393ce" stroke-width="2"/></svg></h2>
<div class="grid uploads" style="top:721px">
  <div class="card"><div class="thumb" role="img" aria-label="Snowy field under a pale sky" style="background:linear-gradient(180deg,#c9d4de,#e8ecef 60%,#9aa3a8)"><div class="play"><svg width="18" height="20" viewBox="0 0 18 20"><polygon points="2,1 16,10 2,19" fill="none" stroke="#fff" stroke-width="2"/></svg></div></div><div class="card-label">Guest Photo Montage</div></div>
  <div class="card"><div class="thumb" role="img" aria-label="Performers on stage in green costumes" style="background:linear-gradient(135deg,#3aa848,#8ccf6a 40%,#2b3a2a)"><div class="play"><svg width="18" height="20" viewBox="0 0 18 20"><polygon points="2,1 16,10 2,19" fill="none" stroke="#fff" stroke-width="2"/></svg></div></div><div class="card-label">Navruz 2017</div></div>
  <div class="card"><div class="thumb" role="img" aria-label="Gallery storefront sign against a blue sky" style="background:linear-gradient(180deg,#7fb3e0,#c9a86a 55%,#3b2f22)"><div class="play"><svg width="18" height="20" viewBox="0 0 18 20"><polygon points="2,1 16,10 2,19" fill="none" stroke="#fff" stroke-width="2"/></svg></div></div><div class="card-label">Cedar Row Gallery</div></div>
  <div class="card"><div class="thumb" role="img" aria-label="Purple market stall banner" style="background:linear-gradient(135deg,#7c4fb4,#b48ad6 60%,#e4dcee)"><div class="play"><svg width="18" height="20" viewBox="0 0 18 20"><polygon points="2,1 16,10 2,19" fill="none" stroke="#fff" stroke-width="2"/></svg></div></div><div class="card-label">Gus's Berries</div></div>

  <div class="card"><div class="thumb" role="img" aria-label="Green and white farm stand sign" style="background:linear-gradient(180deg,#f2f2ea,#e5e9d8 55%,#2f8a3c)"><div class="play"><svg width="18" height="20" viewBox="0 0 18 20"><polygon points="2,1 16,10 2,19" fill="none" stroke="#fff" stroke-width="2"/></svg></div></div><div class="card-label">Hillcrest Community Garden</div></div>
  <div class="card"><div class="thumb" role="img" aria-label="Farm market booth with a red banner" style="background:linear-gradient(180deg,#a8505a,#d8c8c0 45%,#6b5a50)"><div class="play"><svg width="18" height="20" viewBox="0 0 18 20"><polygon points="2,1 16,10 2,19" fill="none" stroke="#fff" stroke-width="2"/></svg></div></div><div class="card-label">Tall Fern Farm</div></div>
  <div class="card"><div class="thumb" role="img" aria-label="Interview at an outdoor market tent" style="background:linear-gradient(135deg,#7a7a78,#c9b39c 55%,#5a4a40)"><div class="play"><svg width="18" height="20" viewBox="0 0 18 20"><polygon points="2,1 16,10 2,19" fill="none" stroke="#fff" stroke-width="2"/></svg></div></div><div class="card-label">Tide Flats</div></div>
  <div class="card"><div class="thumb" role="img" aria-label="Black sauce booth banner with green lettering" style="background:linear-gradient(135deg,#2a2a2a,#3e4a3a 55%,#8a2a2a)"><div class="play"><svg width="18" height="20" viewBox="0 0 18 20"><polygon points="2,1 16,10 2,19" fill="none" stroke="#fff" stroke-width="2"/></svg></div></div><div class="card-label">Smoky Hollow BBQ Sauce</div></div>

  <div class="card"><div class="thumb" role="img" aria-label="Musicians playing under pink stage light" style="background:linear-gradient(135deg,#2a0a14,#a02a5a 50%,#3a0d1c)"><div class="play"><svg width="18" height="20" viewBox="0 0 18 20"><polygon points="2,1 16,10 2,19" fill="none" stroke="#fff" stroke-width="2"/></svg></div></div><div class="card-label">Marco &amp; Johnny</div></div>
  <div class="card"><div class="thumb" role="img" aria-label="Person flying a kite on a grassy park hill" style="background:linear-gradient(180deg,#b8c4cc,#d6d6ce 55%,#8a8a6a)"><div class="play"><svg width="18" height="20" viewBox="0 0 18 20"><polygon points="2,1 16,10 2,19" fill="none" stroke="#fff" stroke-width="2"/></svg></div></div><div class="card-label">Walk in the Park - Bayside</div></div>
  <div class="card"><div class="thumb" role="img" aria-label="Market vendor in a pink hat" style="background:linear-gradient(135deg,#d6c0a0,#c06a7a 50%,#7a9a5a)"><div class="play"><svg width="18" height="20" viewBox="0 0 18 20"><polygon points="2,1 16,10 2,19" fill="none" stroke="#fff" stroke-width="2"/></svg></div></div><div class="card-label">Parkside Organics</div></div>
  <div class="card"><div class="thumb" role="img" aria-label="Handmade poetry sign at a street stall" style="background:linear-gradient(135deg,#3a3222,#cfc29a 55%,#6a5a3a)"><div class="play"><svg width="18" height="20" viewBox="0 0 18 20"><polygon points="2,1 16,10 2,19" fill="none" stroke="#fff" stroke-width="2"/></svg></div></div><div class="card-label">Poems</div></div>
</div>

<h2 class="section-title" style="top:1296px">COMING SOON<svg width="30" height="6" viewBox="0 0 30 6"><path d="M1 5 Q15 -1 29 5" fill="none" stroke="#0393ce" stroke-width="2"/></svg></h2>
<div class="grid" style="top:1361px">
  <div class="card"><div class="thumb" role="img" aria-label="Cooking demo table in front of a green screen" style="background:linear-gradient(135deg,#2a2a2a,#3aa048 55%,#dcdcdc)"></div><div class="card-label">Maple Kitchen</div></div>
  <div class="card"><div class="thumb" role="img" aria-label="Aerial view of city rooftops" style="background:linear-gradient(180deg,#8aa0a8,#a8705a 50%,#5a6a72)"></div><div class="card-label">Through My Lens Photography</div></div>
  <div class="card"><div class="thumb" role="img" aria-label="Colourful hats and a sewing machine on a table" style="background:linear-gradient(135deg,#3a2a2a,#d85a7a 45%,#e8a040 70%,#2a2a2a)"></div><div class="card-label">Hat Parade</div></div>
  <div class="card"><div class="thumb" role="img" aria-label="Jar of salsa with a spoon" style="background:linear-gradient(135deg,#1e1e1e,#a02a2a 50%,#d8a060 75%,#2a2a2a)"></div><div class="card-label">Rosa's Best Salsa</div></div>
</div>

<h2 class="section-title" style="top:1572px">LATEST EVENTS<svg width="30" height="6" viewBox="0 0 30 6"><path d="M1 5 Q15 -1 29 5" fill="none" stroke="#0393ce" stroke-width="2"/></svg></h2>
<div class="grid" style="top:1636px">
  <div class="card"><div class="thumb" role="img" aria-label="Dancers in yellow skirts performing outdoors" style="background:linear-gradient(180deg,#5a6a3a,#d8b040 60%,#3a3a2a)"></div><div class="card-label">Heritage Fest 2017</div></div>
  <div class="card"><div class="thumb" role="img" aria-label="Kites flying over a grassy field" style="background:linear-gradient(180deg,#b0aea0,#c8c4b0 55%,#5a7a3a)"></div><div class="card-label">Kite Festival</div></div>
  <div class="card"><div class="thumb" role="img" aria-label="Friends in costume at a park by the water" style="background:linear-gradient(135deg,#9ab0c0,#d87aa0 45%,#2a2a2a)"></div><div class="card-label">Alice in Wonderland at Bayside Park</div></div>
  <div class="card"><div class="thumb" role="img" aria-label="Swirling colourful painted mural" style="background:linear-gradient(135deg,#e86a2a,#f0b040 40%,#3a7ab0 75%,#e04a3a)"></div><div class="card-label">Test Events</div></div>
</div>

<div class="feature-media" role="img" aria-label="Keyboard player and drummer performing under pink light">
  <div class="corner-go"><svg width="18" height="18" viewBox="0 0 18 18"><circle cx="9" cy="9" r="8" fill="#fff"/><path d="M7 5 L11 9 L7 13" fill="none" stroke="#0393ce" stroke-width="2"/></svg></div>
</div>
<h3 class="feature-title">MARCO BELLINI AND JOHNNY PRATT</h3>
<p class="feature-text">The Honky-Tonk Rebel Marco Bellini and legendary drummer Johnny Pratt perform for us in Portland They also gave us an interview before the show.</p>

<article class="story" style="top:1860px">
  <div class="story-img" role="img" aria-label="Model on a runway at a mall fashion show" style="background:linear-gradient(180deg,#9a8a70,#d8cfc0 55%,#6a5a48)"><div class="corner-go"><svg width="10" height="10" viewBox="0 0 10 10"><path d="M3 1 L7 5 L3 9" fill="none" stroke="#fff" stroke-width="1.8"/></svg></div></div>
  <h3>The Kalani Spring Fling Fashion Show</h3>
  <p>We experienced a little fashion at the Lakeview Mall hosted by Kalani Fashion Showcasing other local designers as well.</p>
</article>
<article class="story" style="top:1975px">
  <div class="story-img" role="img" aria-label="Seafood company sign on a building" style="background:linear-gradient(180deg,#e8e8e4,#bfbfb8 55%,#4a4a48)"><div class="corner-go"><svg width="10" height="10" viewBox="0 0 10 10"><path d="M3 1 L7 5 L3 9" fill="none" stroke="#fff" stroke-width="1.8"/></svg></div></div>
  <h3>Tide Flats 2017</h3>
  <p>There was lots of fun to be had at the 2017 Tide Flats. There was food, entertainment, vendors, oyster competitions and of course, the chance to pick as many oysters and clams as you wish.</p>
</article>
<article class="story" style="top:2089px">
  <div class="story-img" role="img" aria-label="Herbalist speaking in an interview" style="background:linear-gradient(135deg,#5a5a60,#8a7a7a 55%,#2a2a30)"><div class="corner-go"><svg width="10" height="10" viewBox="0 0 10 10"><path d="M3 1 L7 5 L3 9" fill="none" stroke="#fff" stroke-width="1.8"/></svg></div></div>
  <h3>Willow - Coastal Herbalist</h3>
  <p>We visited Willow as she talks about her journey in becoming an herbalist. She also talks about what she does as an herbalist and the importance of using herbs as a supplement for overall health.</p>
</article>

<div class="contact-band">
  <div class="cell"><span class="ic"><svg width="12" height="16" viewBox="0 0 12 16"><path d="M6 15 C2 10 1 8 1 6 a5 5 0 0 1 10 0 c0 2 -1 4 -5 9z" fill="none" stroke="#fff" stroke-width="1.5"/><circle cx="6" cy="6" r="1.8" fill="#fff"/></svg></span><span>Donec fermentum eleifend erat, at<br>blandit ipsum commodo at.</span></div>
  <div class="cell"><span class="ic"><svg width="14" height="14" viewBox="0 0 14 14"><path d="M3 1 L5.5 1 L6.5 4 L5 5.2 C5.8 7 7 8.2 8.8 9 L10 7.5 L13 8.5 L13 11 C13 12 12 13 11 13 C5.5 12.5 1.5 8.5 1 3 C1 2 2 1 3 1z" fill="#fff"/></svg></span><span>(+91) 999-999-9999<br>(+91) 888-888-8888</span></div>
  <div class="cell"><span class="ic"><svg width="14" height="11" viewBox="0 0 14 11"><rect x="1" y="1" width="12" height="9" fill="none" stroke="#fff" stroke-width="1.4"/><path d="M1 1 L7 6 L13 1" fill="none" stroke="#fff" stroke-width="1.4"/></svg></span><span>info@heytherepinecrest.example<br>support@heytherepinecrest.example</span></div>
</div>

<footer class="site-footer">
  <div class="foot-col" style="left:160px;width:200px">
    <h4>ABOUT US</h4>
    <div class="foot-brand">Hey There Pinecrest</div>
    <p class="foot-text">Lorem ipsum dolor sit amet, consectetur adipiscing elit. Maecenas orci leo, consectetur molestie neque a, venenatis aliquam dolor. Nullam et hendrerit ex. Duis neque purus</p>
  </div>
  <div class="foot-col" style="left:387px;width:222px">
    <h4>SERVICES</h4>
    <ul class="services">
      <li><i class="bullet"><svg width="5" height="6" viewBox="0 0 5 6"><path d="M1 0.5 L4 3 L1 5.5" fill="none" stroke="#2a2a2a" stroke-width="1.3"/></svg></i>People</li>
      <li><i class="bullet"><svg width="5" height="6" viewBox="0 0 5 6"><path d="M1 0.5 L4 3 L1 5.5" fill="none" stroke="#2a2a2a" stroke-width="1.3"/></svg></i>Pinecrest Peeps</li>
      <li><i class="bullet"><svg width="5" height="6" viewBox="0 0 5 6"><path d="M1 0.5 L4 3 L1 5.5" fill="none" stroke="#2a2a2a" stroke-width="1.3"/></svg></i>Events</li>
      <li><i class="bullet"><svg width="5" height="6" viewBox="0 0 5 6"><path d="M1 0.5 L4 3 L1 5.5" fill="none" stroke="#2a2a2a" stroke-width="1.3"/></svg></i>Places</li>
      <li><i class="bullet"><svg width="5" height="6" viewBox="0 0 5 6"><path d="M1 0.5 L4 3 L1 5.5" fill="none" stroke="#2a2a2a" stroke-width="1.3"/></svg></i>Meet the Vendors</li>
      <li><i class="bullet"><svg width="5" height="6" viewBox="0 0 5 6"><path d="M1 0.5 L4 3 L1 5.5" fill="none" stroke="#2a2a2a" stroke-width="1.3"/></svg></i>Meet the Events</li>
      <li><i class="bullet"><svg width="5" height="6" viewBox="0 0 5 6"><path d="M1 0.5 L4 3 L1 5.5" fill="none" stroke="#2a2a2a" stroke-width="1.3"/></svg></i>Scenic Video</li>
      <li><i class="bullet"><svg width="5" height="6" viewBox="0 0 5 6"><path d="M1 0.5 L4 3 L1 5.5" fill="none" stroke="#2a2a2a" stroke-width="1.3"/></svg></i>Roses &amp; Flowers</li>
      <li><i class="bullet"><svg width="5" height="6" viewBox="0 0 5 6"><path d="M1 0.5 L4 3 L1 5.5" fill="none" stroke="#2a2a2a" stroke-width="1.3"/></svg></i>Performance</li>
      <li><i class="bullet"><svg width="5" height="6" viewBox="0 0 5 6"><path d="M1 0.5 L4 3 L1 5.5" fill="none" stroke="#2a2a2a" stroke-width="1.3"/></svg></i>Performance</li>
      <li><i class="bullet"><svg width="5" height="6" viewBox="0 0 5 6"><path d="M1 0.5 L4 3 L1 5.5" fill="none" stroke="#2a2a2a" stroke-width="1.3"/></svg></i>Lighter Side</li>
      <li><i class="bullet"><svg width="5" height="6" viewBox="0 0 5 6"><path d="M1 0.5 L4 3 L1 5.5" fill="none" stroke="#2a2a2a" stroke-width="1.3"/></svg></i>Scenery</li>
      <li><i class="bullet"><svg width="5" height="6" viewBox="0 0 5 6"><path d="M1 0.5 L4 3 L1 5.5" fill="none" stroke="#2a2a2a" stroke-width="1.3"/></svg></i>Quote of the day</li>
      <li><i class="bullet"><svg width="5" height="6" viewBox="0 0 5 6"><path d="M1 0.5 L4 3 L1 5.5" fill="none" stroke="#2a2a2a" stroke-width="1.3"/></svg></i>Water Activity</li>
    </ul>
  </div>
  <div class="foot-col" style="left:610px;width:215px">
    <h4>EVENTS</h4>
    <div class="foot-event"><i role="img" aria-label="Musicians on stage" style="background:linear-gradient(135deg,#3a0d1c,#a02a5a)"></i><span>Marco Bellini and Johnny Pratt</span></div>
    <div class="foot-event"><i role="img" aria-label="Fashion show runway" style="background:linear-gradient(135deg,#9a8a70,#d8cfc0)"></i><span>The Kalani Spring Fling Fashion Show</span></div>
    <div class="foot-event"><i role="img" aria-label="Seafood festival sign" style="background:linear-gradient(135deg,#e8e8e4,#6a6a66)"></i><span>Tide Flats 2017</span></div>
    <div class="foot-event"><i role="img" aria-label="Needle painting artwork" style="background:linear-gradient(135deg,#7a5a4a,#c8a080)"></i><span>Dana Alvarez - Needle Painter</span></div>
  </div>
  <div class="foot-col" style="left:836px;width:202px">
    <h4>NEWSLETTER</h4>
    <p class="foot-text" style="color:var(--blue)">Lorem ipsum dolor sit amet, consectetur adipiscing elit. Maecenas orci leo,</p>
    <div class="newsletter-field"><span>Enter your email address</span><i><svg width="12" height="10" viewBox="0 0 12 10"><path d="M6 1 L10 5 L6 9 M10 5 H1" fill="none" stroke="#fff" stroke-width="1.8"/></svg></i></div>
    <h4 style="margin:30px 0 14px">FOLLOW US ON</h4>
    <div class="foot-social"><i class="dot"></i><i class="dot"></i><i class="dot"></i><i class="dot"></i></div>
  </div>
</footer>
<div class="copyright">© 2008-2017 HEY THERE PINECREST. ALL RIGHT RESERVED</div>

</body>
</html>
```